Modern, Clean website for painting service.

We are working with a company called Brushwell Crafts and building a new website for them.

Some sites to use for content/competitors and inspiration:

https://www.coatvantaged.com
https://ridgeline-hue.com
https://tedvarnokcoating.com

Thank you for taking the time to consider designing a website for us. We are web developers based in Stockton, CA, USA. Most of our projects go through the same process. Understanding this process may help you win a project with us. We custom-code all of our websites in-house. We don’t have any requirements as to what tools you use for your design, but we prefer Figma files. For any design that we label as four-stars, we send it to the client for review. The client picks the final design they want us to use. Once we complete this process, we will continue to show additional clients all the four-star sites and purchase them later. Your designs will have multiple chances to sell. For better chances of success, we ask that you follow these guidelines.

IMAGES:
If you use any images or icons in the design, we ask that you have a link to the asset so we can purchase the image/icon. Most of the designs we submit do not have the customer’s images on them unless they have some great images. Be creative; show us the feeling you are trying to portray with your image choices. Use any royalty-free site you choose. We subscribe to Kelvra and mainly use their images, but we can purchase images outside of Kelvra. PLEASE NOTE: we will not submit designs to clients with watermarks on the images.

FONTS:
We ask that you identify the fonts used in the design. This can be done in a message if you want. We typically use Google Fonts and Kelvra Type.

CONTENT:
We're always open to different content and ideas. We often submit designs with stock images so the client can see our vision. We typically take pictures after the website launch to use their images with our vision. Lorem Ipsum is fine for paragraphs, but we ask that you write the headers in correct English. We want to be able to show the vision and identify the sections of the website.

INSPIRATION:
We typically add a couple of links in the brief of websites we like to help you get started in your design.

REVISIONS:
We do not often ask for revisions of the designs unless we see something in the design that may not appeal to the client. If there are slight changes that we want to make, we do that in the development process.

FEEDBACK:
We rarely give feedback on designs during the design process. We are working on many website projects and do not have the time to provide feedback. We usually respond if your request is well thought out and asks specific questions, but a note asking “feedback, please” usually goes unanswered.

```html
<!DOCTYPE html>
<html lang="en">
<head>
<meta charset="utf-8">
<title>Brushwell Crafts – Painting Services</title>
<link href="https://fonts.googleapis.com/css2?family=Fira+Sans:wght@400;500;600;700&family=Lato:wght@400;700;900&display=swap" rel="stylesheet">
<style>
:root{
  --navy:#1d3f7e;
  --navy-deep:#142a55;
  --red:#a50f2a;
  --ink:#222831;
  --text:#555b66;
  --muted:#8a8f98;
  --light:#f2f2f2;
  --white:#ffffff;
  --footer:#0f1c2a;
  --footer-bar:#dfe5ee;
}
*{box-sizing:border-box;margin:0;padding:0}
html,body{width:1200px;height:4967px;overflow:hidden}
body{position:relative;font-family:"Lato",sans-serif;color:var(--text);background:var(--white)}
.abs{position:absolute}
h1,h2,h3,h4{font-family:"Fira Sans",sans-serif}
.label{font-family:"Lato",sans-serif;font-weight:900;font-size:11px;letter-spacing:.5px;color:var(--red);text-transform:uppercase;display:flex;align-items:center;gap:14px}
.label .dash{display:inline-block;width:48px;height:2px;background:var(--red)}
.section-title{color:var(--navy);font-weight:600;font-size:46px;line-height:1.1;white-space:nowrap}
.btn-red{background:var(--red);color:var(--white);font-weight:700;font-size:13px;border-radius:4px;display:flex;align-items:center;justify-content:center;font-family:"Lato",sans-serif}
.lorem{font-size:12.5px;line-height:24px;color:var(--text)}

/* header */
.topbar{left:0;top:0;width:1200px;height:106px;background:var(--light)}
.brand{left:138px;top:22px;display:flex;align-items:center;gap:8px;font-family:"Fira Sans",sans-serif;font-weight:600;font-size:17px;color:var(--navy)}
.brand .sq{width:20px;height:20px;background:var(--red);border-radius:3px}
.info{display:flex;gap:12px;align-items:flex-start;font-size:11px;line-height:20px;color:var(--text)}
.info b{font-weight:400;text-transform:uppercase;font-size:10.5px;color:var(--ink)}
.quote-btn{left:946px;top:22px;width:167px;height:46px;background:#2f3237;color:var(--white);font-size:11px;font-weight:900;display:flex;align-items:center;justify-content:center;border-radius:3px}
.nav{left:87px;top:73px;width:1026px;height:68px;background:var(--white);border-radius:2px;box-shadow:0 4px 14px rgba(0,0,0,.08);z-index:3}
.nav ul{list-style:none;display:flex;position:absolute;left:35px;top:0;height:68px;align-items:center}
.nav li{font-size:13px;font-weight:700;color:var(--ink);margin-right:56px}
.social{position:absolute;right:32px;top:17px;display:flex;gap:10px}
.social span{width:36px;height:36px;border-radius:3px}

/* hero */
.hero{left:0;top:106px;width:1200px;height:687px;background:linear-gradient(90deg,#6a6560 0%,#8a7446 45%,#b98a1e 75%,#c3901c 100%)}
.hero-shade{left:0;top:106px;width:1200px;height:687px;background:rgba(0,0,0,.25)}
.tag{left:512px;top:328px;width:162px;height:38px;background:var(--navy);color:var(--white);font-size:11px;font-weight:900;display:flex;align-items:center;justify-content:center}
.hero-title{left:250px;top:380px;width:700px;text-align:center;color:var(--white);font-size:61px;font-weight:600;line-height:70px;white-space:nowrap}
.hero-btn{left:508px;top:547px;width:170px;height:48px;border:2px solid #d8d8d8;color:var(--white);font-size:11px;font-weight:900;display:flex;align-items:center;justify-content:center;border-radius:3px}
.arrow-box{width:62px;height:62px;background:var(--white);display:flex;align-items:center;justify-content:center}

/* about */
.about-ring{left:96px;top:924px;width:444px;height:432px;border-radius:50%;background:var(--navy)}
.about-photo{left:112px;top:922px;width:430px;height:430px;border-radius:50%;background:linear-gradient(135deg,#d9dde0,#9ea7ad 55%,#6d7b5c)}
.about-badge{left:433px;top:1246px;width:100px;height:100px;border-radius:50%;background:var(--white);box-shadow:0 4px 14px rgba(0,0,0,.15)}

/* services */
.services{left:0;top:1456px;width:1200px;height:826px;background:var(--light)}
.svc-card{width:320px;height:313px;border-radius:6px;overflow:hidden}
.svc-card .ph{position:absolute;inset:0}
.svc-card .ov{position:absolute;inset:0;background:linear-gradient(180deg,rgba(0,0,0,.15),rgba(20,20,20,.55))}
.svc-icon{position:absolute;left:34px;top:46px;width:66px;height:66px;background:var(--white);border-radius:8px;display:flex;align-items:center;justify-content:center}
.svc-card h3{position:absolute;left:34px;top:148px;color:var(--white);font-size:22px;font-weight:600;white-space:nowrap}
.svc-card p{position:absolute;left:34px;top:212px;color:var(--white);font-size:12px;white-space:nowrap}
.svc-card .more{position:absolute;left:34px;top:250px;color:var(--white);font-size:14px;font-weight:900}
.svc-card .line{position:absolute;left:34px;top:280px;width:252px;height:2px;background:var(--red)}
.sq-arrow{width:46px;height:62px;background:var(--white);border:1px solid #e2e2e2;display:flex;align-items:center;justify-content:center}

/* cta band */
.cta{left:95px;top:2178px;width:1014px;height:208px;border-radius:6px;background:linear-gradient(90deg,#1a2942 0%,#243a5e 45%,#1c3050 100%)}
.cta h3{position:absolute;left:55px;top:82px;color:var(--white);font-size:22px;font-weight:600;line-height:28px}
.cta .ghost{position:absolute;left:588px;top:84px;width:166px;height:52px;border:1.5px solid #e0e0e0;color:var(--white);font-size:12px;font-weight:700;display:flex;align-items:center;justify-content:center}
.cta .phone{position:absolute;left:758px;top:84px;width:204px;height:52px;background:var(--white);color:var(--ink);font-size:13px;display:flex;align-items:center;justify-content:center;gap:10px}

/* projects */
.proj{height:403px}
.caption{left:249px;top:2878px;width:598px;height:75px;background:var(--white);color:var(--navy);font-family:"Fira Sans",sans-serif;font-weight:600;font-size:22px;display:flex;align-items:center;padding-left:38px}
.cap-arrow{left:847px;top:2878px;width:81px;height:75px;background:var(--red);display:flex;align-items:center;justify-content:center}

/* testimonials */
.testi{left:0;top:3057px;width:1200px;height:533px;background:var(--light)}
.testi-dark{left:0;top:3057px;width:334px;height:533px;background:linear-gradient(180deg,#2d2d2d,#3a3a3a)}
.review{width:345px;height:208px;background:var(--white);border-radius:8px;box-shadow:0 4px 14px rgba(0,0,0,.08);padding:22px 22px}
.review p{font-size:12px;line-height:24px;color:var(--text)}
.review .who{position:absolute;left:22px;top:146px;display:flex;align-items:center;gap:14px;font-size:12px;font-weight:700;color:var(--ink)}
.avatar{width:44px;height:44px;border-radius:50%;background:linear-gradient(135deg,#c9c2b6,#7b7368)}
.review .q{position:absolute;right:26px;top:146px;font-family:"Fira Sans",sans-serif;font-weight:700;font-size:40px;line-height:40px;color:var(--navy)}
.dot{width:8px;height:8px;border-radius:50%;background:#b5bcc6}

/* contact */
.contact-box{left:93px;top:3845px;width:1012px;height:412px;background:var(--white);box-shadow:0 6px 24px rgba(0,0,0,.1)}
.contact-photo{left:93px;top:3845px;width:416px;height:412px;background:linear-gradient(135deg,#e3e3e0,#a98a6e 55%,#5b4a3e)}
.call{left:285px;top:4181px;width:198px;height:54px;background:var(--white);box-shadow:0 4px 12px rgba(0,0,0,.12);display:flex;align-items:center;justify-content:center;gap:10px;font-size:16px;font-weight:700;color:var(--ink)}
.field{height:49px;border:1px solid #dadada;border-radius:3px;font-size:12px;color:var(--text);display:flex;align-items:center;padding-left:18px}

/* footer */
.footer{left:0;top:4404px;width:1200px;height:503px;background:var(--footer)}
.strip{left:85px;top:4404px;width:1028px;height:152px;background:var(--white);display:flex}
.strip div{flex:1;display:flex;flex-direction:column;align-items:center;justify-content:center;gap:12px;font-weight:700;font-size:15px;color:var(--ink);border-right:1px solid #e4e4e4;margin:24px 0}
.strip div:last-child{border-right:none}
.foot-h{font-family:"Fira Sans",sans-serif;font-weight:600;font-size:17px;color:var(--white)}
.foot-t{font-size:12px;line-height:33px;color:#8d97a6}
.bottom{left:0;top:4907px;width:1200px;height:60px;background:var(--footer-bar)}
</style>
</head>
<body>

<!-- header -->
<div class="abs topbar"></div>
<div class="abs brand"><span class="sq"></span>Brushwell Crafts</div>
<div class="abs info" style="left:430px;top:22px">
  <svg width="24" height="30" viewBox="0 0 24 30"><path d="M12 1C6 1 2 5.5 2 11c0 7 10 18 10 18s10-11 10-18C22 5.5 18 1 12 1z" fill="#333"/><circle cx="12" cy="11" r="4" fill="#f2f2f2"/></svg>
  <div><b>Location</b><br>48 Orchard Ln, LA</div>
</div>
<div class="abs" style="left:652px;top:20px;width:1px;height:46px;background:#cfcfcf"></div>
<div class="abs info" style="left:676px;top:22px">
  <svg width="36" height="34" viewBox="0 0 36 34"><circle cx="18" cy="18" r="13" fill="none" stroke="#333" stroke-width="2.5"/><path d="M18 10v9l6 3" fill="none" stroke="#333" stroke-width="2.5"/><path d="M4 8l5-5M32 8l-5-5" stroke="#333" stroke-width="2.5"/></svg>
  <div><b>Office Hours</b><br>9.00 to 7.00 [Ssun: closed]</div>
</div>
<div class="abs quote-btn">REQUEST A QUOTE</div>

<nav class="abs nav">
  <ul><li>Home</li><li>About Us</li><li>Services</li><li>Gallery</li><li>Our Team</li><li>Contact Us</li></ul>
  <div class="social"><span style="background:#3c5a9a"></span><span style="background:#d1203a"></span><span style="background:#2fa6df"></span></div>
</nav>

<!-- hero -->
<div class="abs hero" role="img" aria-label="Painter holding a paint roller in front of a mustard yellow wall"></div>
<div class="abs hero-shade"></div>
<div class="abs tag">WELCOME</div>
<h1 class="abs hero-title">Unleashing the<br>power of color</h1>
<div class="abs hero-btn">ABOUT COMPANY</div>
<div class="abs arrow-box" style="left:44px;top:488px"><svg width="24" height="16" viewBox="0 0 24 16"><path d="M23 8H2M8 1L1 8l7 7" fill="none" stroke="#999" stroke-width="1.6"/></svg></div>
<div class="abs arrow-box" style="left:1094px;top:488px"><svg width="24" height="16" viewBox="0 0 24 16"><path d="M1 8h21M16 1l7 7-7 7" fill="none" stroke="#999" stroke-width="1.6"/></svg></div>

<!-- about -->
<div class="abs about-ring"></div>
<div class="abs about-photo" role="img" aria-label="Painter on a ladder in a safety vest painting a white wall"></div>
<div class="abs about-badge"></div>
<div class="abs label" style="left:610px;top:939px">About Us <span class="dash"></span></div>
<h2 class="abs section-title" style="left:608px;top:973px;font-size:47px;line-height:61px">Where expertise<br>meets elegance</h2>
<p class="abs lorem" style="left:610px;top:1104px;width:440px">Lorem ipsum dolor sit amet, consectetur adipiscing elit, sed do eiusmo empor incididunt ut abore et dolore magna aliqua. Ut enim ad minim iam, quis nostrud exercitation ullamco</p>
<p class="abs lorem" style="left:610px;top:1187px;width:440px">Lorem ipsum dolor sit amet, consectetur adipiscing elit, sed do eiusmo empor incididunt ut abore et dolore magna aliqua. Ut enim ad minim iam, quis nostrud exercitation ullamco</p>
<div class="abs btn-red" style="left:610px;top:1294px;width:169px;height:45px">Apply Now</div>

<!-- services -->
<div class="abs services"></div>
<div class="abs label" style="left:89px;top:1543px">Services <span class="dash"></span></div>
<h2 class="abs section-title" style="left:87px;top:1577px">Services We Offer</h2>
<div class="abs sq-arrow" style="left:998px;top:1559px"><svg width="10" height="16" viewBox="0 0 10 16"><path d="M8 1L2 8l6 7" fill="none" stroke="#222" stroke-width="2"/></svg></div>
<div class="abs sq-arrow" style="left:1050px;top:1559px"><svg width="10" height="16" viewBox="0 0 10 16"><path d="M2 1l6 7-6 7" fill="none" stroke="#222" stroke-width="2"/></svg></div>

<div class="abs svc-card" style="left:91px;top:1682px">
  <div class="ph" role="img" aria-label="Painter in a cap rolling paint on a wall" style="background:linear-gradient(135deg,#cfcac4,#8e8276)"></div><div class="ov"></div>
  <div class="svc-icon"><svg width="32" height="32" viewBox="0 0 32 32"><path d="M16 4l11 8-4 14H9L5 12z" fill="none" stroke="#1d3f7e" stroke-width="2"/><circle cx="16" cy="16" r="3" fill="none" stroke="#1d3f7e" stroke-width="2"/></svg></div>
  <h3>Residential Painting</h3><p>Lorem ipsum dolor sit amet, consectetur</p><div class="more">Read More</div><div class="line"></div>
</div>
<div class="abs svc-card" style="left:438px;top:1682px">
  <div class="ph" role="img" aria-label="Worker painting trim on a commercial building" style="background:linear-gradient(135deg,#c8cdc6,#6d7261)"></div><div class="ov"></div>
  <div class="svc-icon"><svg width="32" height="32" viewBox="0 0 32 32"><path d="M8 24l12-16 4 3-12 16H8z" fill="none" stroke="#1d3f7e" stroke-width="2"/><path d="M6 28h20" stroke="#1d3f7e" stroke-width="2"/></svg></div>
  <h3>Commercial Painting</h3><p>Lorem ipsum dolor sit amet, consectetur</p><div class="more">Read More</div><div class="line"></div>
</div>
<div class="abs svc-card" style="left:785px;top:1682px">
  <div class="ph" role="img" aria-label="Interior room with wooden ceiling being coated" style="background:linear-gradient(135deg,#a9653d,#e2ddd6 60%,#9a948d)"></div><div class="ov"></div>
  <div class="svc-icon"><svg width="32" height="32" viewBox="0 0 32 32"><circle cx="11" cy="11" r="4" fill="none" stroke="#1d3f7e" stroke-width="2"/><circle cx="22" cy="11" r="4" fill="none" stroke="#1d3f7e" stroke-width="2"/><path d="M3 26c0-5 4-8 8-8s8 3 8 8M14 20c2-2 4-2 8-2 4 0 7 3 7 8" fill="none" stroke="#1d3f7e" stroke-width="2"/></svg></div>
  <h3>Specialized Coating</h3><p>Lorem ipsum dolor sit amet, consectetur</p><div class="more">Read More</div><div class="line"></div>
</div>
<div class="abs btn-red" style="left:513px;top:2068px;width:168px;height:46px">Contact Us</div>

<!-- cta -->
<div class="abs cta" role="img" aria-label="Modern glass office building at dusk">
  <h3>Precision painting for<br>perfectionists</h3>
  <div class="ghost">Get A Quote</div>
  <div class="phone"><svg width="16" height="16" viewBox="0 0 24 24"><path d="M5 2h4l2 5-3 2c1 3 4 6 7 7l2-3 5 2v4c0 1-1 2-2 2C10 21 3 14 3 4c0-1 1-2 2-2z" fill="#222"/></svg>+ 012 555 - 01930</div>
</div>

<!-- projects -->
<div class="abs label" style="left:507px;top:2452px"><span class="dash"></span>Our Blog<span class="dash"></span></div>
<h2 class="abs section-title" style="left:0;top:2476px;width:1200px;text-align:center">Latest Projects</h2>
<div class="abs proj" style="left:0;top:2591px;width:170px;background:linear-gradient(135deg,#eef0f2,#a9b2bb)" role="img" aria-label="Bright office lobby interior"></div>
<div class="abs proj" style="left:208px;top:2591px;width:758px;background:linear-gradient(180deg,#5f95d6 0%,#8fb9e6 40%,#c9b7a3 60%,#a89680 100%)" role="img" aria-label="Painter working on the facade of a two-storey house"></div>
<div class="abs proj" style="left:1001px;top:2591px;width:199px;background:linear-gradient(180deg,#222 0 4%,#e9e6e1 4%,#bfc3c2 96%,#222 96%)" role="img" aria-label="Freshly painted living room"></div>
<div class="abs arrow-box" style="left:84px;top:2754px;width:66px;height:92px"><svg width="12" height="20" viewBox="0 0 12 20"><path d="M10 1L2 10l8 9" fill="none" stroke="#222" stroke-width="2"/></svg></div>
<div class="abs arrow-box" style="left:1024px;top:2754px;width:66px;height:92px"><svg width="12" height="20" viewBox="0 0 12 20"><path d="M2 1l8 9-8 9" fill="none" stroke="#222" stroke-width="2"/></svg></div>
<div class="abs caption">Project 567 in ABC State</div>
<div class="abs cap-arrow"><svg width="30" height="16" viewBox="0 0 30 16"><path d="M1 8h27M21 1l7 7-7 7" fill="none" stroke="#fff" stroke-width="2"/></svg></div>

<!-- testimonials -->
<div class="abs testi"></div>
<div class="abs testi-dark" role="img" aria-label="Dim workshop backdrop"></div>
<div class="abs label" style="left:575px;top:3119px"><span class="dash"></span>Testimonials<span class="dash"></span></div>
<h2 class="abs section-title" style="left:430px;top:3145px">Reviews from Clients</h2>

<div class="abs review" style="left:135px;top:3258px">
  <p>Lorem ipsum dolorLorem ipsum dolor sit amet, co nsectetur adipiscing elit, sed do eiusmod tempor incididunt ut labore et dolore magna aliqua. Ut en im ad minim veniam, quis nostrud exercitation ull</p>
  <div class="who"><span class="avatar"></span>Nora Vell</div><div class="q">”</div>
</div>
<div class="abs review" style="left:500px;top:3258px;border-bottom:3px solid var(--red)">
  <p>Lorem ipsum dolorLorem ipsum dolor sit amet, co nsectetur adipiscing elit, sed do eiusmod tempor incididunt ut labore et dolore magna aliqua. Ut en im ad minim veniam, quis nostrud exercitation ull</p>
  <div class="who"><span class="avatar"></span>Nora Vell</div><div class="q">”</div>
</div>
<div class="abs review" style="left:868px;top:3258px;width:332px;border-radius:8px 0 0 8px">
  <p>Lorem ipsum dolorLorem ipsum dolor sit amet, co nsectetur adipiscing elit, sed do eiusmod tempor incididunt ut labore et dolore magna aliqua. Ut en im ad minim veniam, quis nostrud exercitation ull</p>
  <div class="who"><span class="avatar"></span>Nora Vell</div><div class="q">”</div>
</div>
<div class="abs" style="left:628px;top:3505px;width:16px;height:16px;border-radius:50%;border:1.5px solid var(--navy)"></div>
<div class="abs dot" style="left:632px;top:3509px;background:var(--navy)"></div>
<div class="abs dot" style="left:662px;top:3509px"></div>
<div class="abs dot" style="left:692px;top:3509px"></div>
<div class="abs dot" style="left:722px;top:3509px"></div>

<!-- contact -->
<div class="abs label" style="left:530px;top:3713px"><span class="dash"></span>Contact Us<span class="dash"></span></div>
<h2 class="abs section-title" style="left:0;top:3739px;width:1200px;text-align:center">Get in touch with us</h2>
<div class="abs contact-box"></div>
<div class="abs contact-photo" role="img" aria-label="Two painters with rollers at a white wall"></div>
<div class="abs call"><svg width="18" height="18" viewBox="0 0 24 24"><path d="M5 2h4l2 5-3 2c1 3 4 6 7 7l2-3 5 2v4c0 1-1 2-2 2C10 21 3 14 3 4c0-1 1-2 2-2z" fill="#222"/></svg>1800-555-019</div>
<h3 class="abs" style="left:552px;top:3893px;font-size:23px;font-weight:600;color:var(--ink)">Get Free Consultation</h3>
<p class="abs" style="left:552px;top:3930px;width:500px;font-size:13px;line-height:25px;color:var(--text)">Get a free consultation from our experts, Our customer support team help you 24/7. Don't hesitate.</p>
<div class="abs field" style="left:552px;top:4010px;width:502px">Your Name</div>
<div class="abs field" style="left:552px;top:4080px;width:238px">Your Email</div>
<div class="abs field" style="left:816px;top:4080px;width:238px">Message</div>
<div class="abs btn-red" style="left:552px;top:4147px;width:502px;height:50px;font-size:11px;font-weight:900;gap:8px">GET IN TOUCH <svg width="18" height="10" viewBox="0 0 18 10"><path d="M1 5h15M12 1l4 4-4 4" fill="none" stroke="#fff" stroke-width="1.5"/></svg></div>

<!-- footer -->
<svg class="abs" style="left:0;top:4370px" width="1200" height="36" viewBox="0 0 1200 36"><path d="M118 0L1115 20V36H110z" fill="#e3e8ef"/></svg>
<div class="abs footer"></div>
<div class="abs strip">
  <div><svg width="44" height="40" viewBox="0 0 44 40"><path d="M22 3c-6 0-10 4-10 10 0 7 10 17 10 17s10-10 10-17c0-6-4-10-10-10z" fill="none" stroke="#a50f2a" stroke-width="2"/><circle cx="22" cy="13" r="4" fill="none" stroke="#a50f2a" stroke-width="2"/><path d="M8 28l-6 10h40l-6-10" fill="none" stroke="#a50f2a" stroke-width="2"/></svg>Come to Our Location</div>
  <div><svg width="44" height="40" viewBox="0 0 44 40"><path d="M4 16l18-13 18 13v21H4z" fill="none" stroke="#a50f2a" stroke-width="2"/><path d="M4 16l18 12 18-12" fill="none" stroke="#a50f2a" stroke-width="2"/><rect x="12" y="9" width="20" height="12" fill="none" stroke="#a50f2a" stroke-width="2"/></svg>Send Us an Email</div>
  <div><svg width="44" height="40" viewBox="0 0 24 24"><path d="M5 2h4l2 5-3 2c1 3 4 6 7 7l2-3 5 2v4c0 1-1 2-2 2C10 21 3 14 3 4c0-1 1-2 2-2z" fill="none" stroke="#a50f2a" stroke-width="1.3"/></svg>Give Us a Call</div>
</div>

<div class="abs" style="left:84px;top:4640px;display:flex;align-items:center;gap:10px;font-family:'Fira Sans',sans-serif;font-weight:600;font-size:24px;color:var(--white)"><span style="width:22px;height:22px;background:var(--white);border-radius:3px"></span>Brushwell Crafts</div>
<p class="abs" style="left:84px;top:4746px;width:310px;font-size:12.5px;line-height:22px;color:#8d97a6">Lorem ipsum dolor sit amet, consectetur adipi ng elit, sed do eiusmod tempor incididunt ut la re et dolore magna aliqua. Ut enim ad minim ve am, quis nostrud exercitation ullamco laboris</p>

<h4 class="abs foot-h" style="left:438px;top:4615px">Visit Our Place</h4>
<div class="abs foot-t" style="left:438px;top:4676px;line-height:22px">17 Maple Row<br>Suite 4, 10021, USA</div>
<div class="abs" style="left:438px;top:4737px;font-size:11px;font-weight:700;color:#c3cad4;text-decoration:underline">FIND US ON MAP</div>
<div class="abs" style="left:438px;top:4793px;width:306px;height:42px;border:1px solid #56606d;display:flex">
  <div style="flex:1;font-size:11px;color:#aab2bd;display:flex;align-items:center;padding-left:12px">Enter Your Email...</div>
  <div style="width:100px;border-left:1px solid #56606d;font-size:11px;font-weight:700;color:var(--red);display:flex;align-items:center;justify-content:center">SUBSCRIBE</div>
</div>

<h4 class="abs foot-h" style="left:789px;top:4615px">Useful Links</h4>
<div class="abs foot-t" style="left:789px;top:4677px">About Us<br>Practice areas<br>Why Choose Us<br>How it works<br>News &amp; Updates</div>
<div class="abs foot-t" style="left:959px;top:4677px">Testimonials<br>FAQs<br>Cookies<br>Contact Us<br>Privacy Policy</div>

<div class="abs bottom"></div>
<div class="abs" style="left:86px;top:4928px;font-size:13px;color:var(--ink)">Brushwell Crafts</div>
<div class="abs" style="left:1034px;top:4932px;display:flex;gap:14px">
  <span style="width:8px;height:8px;border-radius:50%;background:var(--ink)"></span><span style="width:8px;height:8px;border-radius:50%;background:var(--ink)"></span><span style="width:8px;height:8px;border-radius:50%;background:var(--ink)"></span><span style="width:8px;height:8px;border-radius:50%;background:var(--ink)"></span>
</div>
<div class="abs" style="left:1138px;top:4888px;width:50px;height:50px;background:var(--red);border-radius:3px;display:flex;align-items:center;justify-content:center"><svg width="18" height="12" viewBox="0 0 18 12"><path d="M1 11L9 2l8 9z" fill="#fff"/></svg></div>

</body>
</html>
```